Two (Similar) Posters - Both 11" x 17"

We are looking for two posters - both 11" x 17" (vertical orientation) - to promote two consecutive, cardiology-related events:

Poster #1) The Inaugural New York ROC Brainbuzz Competition, Cocktail Reception and Whiskey Tasting (http://hb-pvl.org/brainbuzz-and-reception)

and

Poster #2) The 89th Annual Scientific Session and 27th Annual Meeting (http://hb-pvl.org/2017annualmtg)

#1 is a cocktail party with a whiskey tasting that will also feature a gameshow-like event with the med students, and #2 is an educational conference for doctors

Target Market(s)

Healthcare providers (Please do not include stock images of medical professionals; in fact, please use caution with any stock imagery, as it most likely will not be appropriate.)

Industry/Entity Type

Education

Colors

Designer to choose colors to be used in the design.

Requirements
Must have
• Each poster design should include:
• - the 4 logos of the participating organizations (I can upload various other versions if needed) along with the "wording" that goes alongside each one (see "STD_small" image as an example)
• - name of event
• - date, time and location
• - where to register
• - where to get more information
• - some artistic flavor or detailing
• Final (raw) files in an .ai, .psd, .eps or .idml format are required upon project completion.
Nice to have
• It's not crucial that these two posters "match," but it would be nice if they at least coordinated with each other. Would be nice if the designer could stay close to our color scheme (can be found here - http://hb-pvl.org/), but this isn't crucial. Posters should be upscale, neat and professional.
Should not have
• Should not be too difficult to read. These are posters that will likely be hanging on a bulletin board in hospital staff break rooms. Should not be too cartoon-like or silly. The two should not look EXACTLY the same in case people think that they are the same poster.

```html
<!DOCTYPE html>
<html lang="en">
<head>
<meta charset="utf-8">
<title>ROC Brainbuzz Competition Poster</title>
<link href="https://fonts.googleapis.com/css2?family=Crimson+Pro:wght@600;700&display=swap" rel="stylesheet">
<style>
  :root {
    --backdrop: #2a2a2a;
    --navy: #0f1c3a;
    --navy-deep: #0a142c;
    --gold: #e2b93b;
    --gold-light: #f3d75a;
    --gold-dark: #c99a27;
    --badge: #f3d750;
    --ink: #0d1228;
    --white: #ffffff;
    --seal: #1e2f62;
  }
  * { margin: 0; padding: 0; box-sizing: border-box; }
  html, body { width: 1200px; height: 1200px; overflow: hidden; }
  body {
    background: var(--backdrop);
    font-family: "Crimson Pro", Georgia, serif;
    font-weight: 700;
    position: relative;
  }
  .poster {
    position: absolute;
    left: 257px; top: 70px;
    width: 686px; height: 1060px;
    background: linear-gradient(90deg, var(--gold-dark), var(--gold-light) 50%, var(--gold-dark));
  }
  .poster__field {
    position: absolute;
    left: 8px; top: 7px; right: 11px; height: 885px;
    background: radial-gradient(ellipse at 50% 40%, #16264c 0%, var(--navy) 55%, var(--navy-deep) 100%);
  }
  .flourish {
    position: absolute;
    left: 163px; width: 360px; height: 32px;
    border-radius: 16px;
    background: linear-gradient(90deg, var(--gold-dark), var(--gold-light) 50%, var(--gold-dark));
  }
  .flourish--top { top: 84px; }
  .flourish--bottom { top: 316px; }
  .text-center {
    position: absolute; left: 0; right: 0;
    text-align: center; color: var(--white);
  }
  .event-title {
    top: 133px;
    font-size: 26px; line-height: 34px;
    text-transform: uppercase; letter-spacing: 0.2px;
  }
  .event-when {
    top: 362px;
    font-size: 27px; line-height: 37px;
    text-transform: uppercase;
  }
  .event-where {
    top: 450px;
    font-size: 21px;
  }
  .price-badge {
    position: absolute;
    left: 185px; top: 486px;
    width: 312px; height: 312px;
  }
  .price-badge svg { position: absolute; inset: 0; }
  .price-badge__text {
    position: absolute; inset: 0;
    display: flex; flex-direction: column; align-items: center; justify-content: center;
    color: var(--ink); text-align: center;
    font-size: 25px; line-height: 38px;
  }
  .price-badge__big { font-size: 35px; line-height: 44px; }
  .partners {
    position: absolute; left: 0; right: 0; top: 830px; height: 112px;
  }
  .partner {
    position: absolute; top: 0;
    width: 112px; height: 112px; border-radius: 50%;
    background: var(--seal);
    border: 3px solid var(--white);
    display: flex; align-items: center; justify-content: center;
    padding: 14px;
    color: var(--white);
    font-size: 12px; line-height: 14px; text-align: center;
  }
  .contact {
    top: 964px;
    color: var(--ink);
    font-size: 16.5px; line-height: 24px; font-weight: 600;
  }
  .register {
    top: 1018px;
    color: var(--ink);
    font-size: 22px;
  }
</style>
</head>
<body>
  <main class="poster">
    <div class="poster__field"></div>

    <div class="flourish flourish--top" role="img" aria-label="Gold filigree ornament"></div>

    <h1 class="text-center event-title">
      The Inaugural New York<br>ROC Brainbuzz Competition,<br>Cocktail Reception &amp;<br>Whiskey Tasting
    </h1>

    <div class="flourish flourish--bottom" role="img" aria-label="Gold filigree ornament"></div>

    <p class="text-center event-when">Wednesday,&nbsp; Dec. 6th, 2017<br>6:30 P.M. to 10:30 P.M.</p>
    <p class="text-center event-where">Oak &amp; Ember, 14 E 41st St, New York, NY 10017</p>

    <div class="price-badge">
      <svg viewBox="-156 -156 312 312" aria-hidden="true">
        <g fill="var(--badge)">
          <circle r="150"/>
          <circle cx="128" cy="0" r="28"/><circle cx="118.3" cy="49" r="28"/>
          <circle cx="90.5" cy="90.5" r="28"/><circle cx="49" cy="118.3" r="28"/>
          <circle cx="0" cy="128" r="28"/><circle cx="-49" cy="118.3" r="28"/>
          <circle cx="-90.5" cy="90.5" r="28"/><circle cx="-118.3" cy="49" r="28"/>
          <circle cx="-128" cy="0" r="28"/><circle cx="-118.3" cy="-49" r="28"/>
          <circle cx="-90.5" cy="-90.5" r="28"/><circle cx="-49" cy="-118.3" r="28"/>
          <circle cx="0" cy="-128" r="28"/><circle cx="49" cy="-118.3" r="28"/>
          <circle cx="90.5" cy="-90.5" r="28"/><circle cx="118.3" cy="-49" r="28"/>
        </g>
      </svg>
      <div class="price-badge__text">
        <span class="price-badge__big">FREE</span>
        <span>for HBPVL/</span>
        <span>PVL Members and</span>
        <span class="price-badge__big">$30</span>
        <span>for Non-Members</span>
        <span>and Guests</span>
      </div>
    </div>

    <div class="partners">
      <div class="partner" style="left:81px">Pavilion College of Cardiology</div>
      <div class="partner" style="left:221px">Hudson–Lima Chapter Exchange</div>
      <div class="partner" style="left:351px">Hudson Cardiac Center</div>
      <div class="partner" style="left:487px">Metro Cardiological Society</div>
    </div>

    <p class="text-center contact">For more information or to inquire about becoming an exhibitor,<br>call (212) 555-0148 or email ask@hb-pvl.org</p>
    <p class="text-center register">Register online at hb-pvl.org</p>
  </main>
</body>
</html>
```